New modern business card design

To design a brand new business card that's clean & modern in terms of layout.
I have attached our company logo and also basic information regarding what is needed on the card that also needs to be editable.

Target Market(s)

motor trade

Contact Information for Business Card

logo, name, title, tel, mob, email, address, www, all information is in the word.doc file

Requirements
Must have
• white background
Nice to have
• Nice clean font

```html
<!DOCTYPE html>
<html lang="en">
<head>
<meta charset="utf-8">
<title>Hexbolt Removal Ltd – Business Card</title>
<link rel="stylesheet" href="https://fonts.googleapis.com/css2?family=Michroma&family=Arimo:wght@400;500&display=swap">
<style>
  :root {
    --brand-blue: #2a74c0;
    --brand-blue-dark: #1f63aa;
    --pattern-blue: #3a86d0;
    --steel-grey: #b5b7ba;
    --ink: #1c1c1c;
    --paper: #ffffff;
    --backdrop: #e4e6e9;
  }
  * { box-sizing: border-box; margin: 0; padding: 0; }
  html, body { width: 1200px; height: 902px; overflow: hidden; }
  body {
    background: var(--backdrop);
    display: flex; flex-direction: column; align-items: center; justify-content: center;
    gap: 40px;
    font-family: "Arimo", Arial, sans-serif;
  }
  .card {
    position: relative; width: 680px; height: 389px; overflow: hidden;
    box-shadow: 0 6px 18px rgba(0,0,0,.18);
  }

  /* Reverse side */
  .card--back { background: var(--brand-blue); }
  .card__pattern {
    position: absolute; inset: 0;
    background: linear-gradient(135deg, var(--pattern-blue), var(--brand-blue) 55%, var(--brand-blue-dark));
  }
  .back-wordmark {
    position: absolute; right: 48px; top: 50%; transform: translateY(-50%);
    display: flex; align-items: center; gap: 12px;
    font-family: "Michroma", sans-serif; font-size: 20px; color: var(--paper); letter-spacing: 1px;
    white-space: nowrap;
  }
  .back-wordmark__square { width: 22px; height: 22px; background: var(--paper); }

  /* Front side */
  .card--front { background: var(--paper); color: var(--ink); }
  .side-bars { position: absolute; left: 0; top: 120px; width: 52px; }
  .side-bars span { display: block; height: 12px; background: var(--steel-grey); margin-bottom: 10px; }
  .name-plate {
    position: absolute; left: 62px; top: 108px; width: 280px; padding: 13px 18px;
    background: var(--brand-blue); color: var(--paper);
    font-family: "Michroma", sans-serif; text-transform: uppercase; white-space: nowrap;
  }
  .name-plate__name { font-size: 15px; letter-spacing: .5px; }
  .name-plate__title { font-size: 11px; margin-top: 6px; letter-spacing: .5px; }

  .wordmark {
    position: absolute; right: 44px; top: 36px; text-align: center;
  }
  .wordmark__name {
    display: flex; align-items: center; gap: 10px; white-space: nowrap;
    font-family: "Michroma", sans-serif; font-size: 18px; color: var(--brand-blue); letter-spacing: 1px;
  }
  .wordmark__square { width: 18px; height: 18px; background: var(--brand-blue); }
  .wordmark__rule { height: 2px; background: var(--brand-blue); margin-top: 8px; }
  .wordmark__ltd {
    font-family: "Michroma", sans-serif; font-size: 11px; color: var(--brand-blue);
    letter-spacing: 6px; margin-top: 4px;
  }

  .address-rule { position: absolute; right: 40px; top: 182px; width: 300px; height: 2px; background: var(--steel-grey); }
  .address {
    position: absolute; right: 40px; top: 194px; text-align: right;
    font-size: 14px; line-height: 1.45; font-style: normal;
  }
  .address__web { margin-top: 10px; display: block; }

  .divider { position: absolute; left: 0; top: 262px; width: 370px; height: 2px; background: var(--brand-blue); }

  .contacts { position: absolute; left: 48px; top: 274px; list-style: none; font-size: 15px; }
  .contacts li { display: flex; align-items: center; gap: 10px; height: 22px; }
  .contacts svg { width: 14px; height: 14px; fill: var(--brand-blue); }

  .foot-band { position: absolute; left: 0; right: 0; bottom: 0; height: 14px; background: var(--brand-blue); }
  .foot-accent {
    position: absolute; right: 0; bottom: 14px; width: 150px; height: 12px; background: var(--steel-grey);
    clip-path: polygon(12% 0, 100% 0, 100% 100%, 0 100%);
  }
</style>
</head>
<body>

  <section class="card card--back" aria-label="Card reverse">
    <div class="card__pattern" role="img" aria-label="Repeating tone-on-tone brand pattern across the blue background"></div>
    <div class="back-wordmark"><span class="back-wordmark__square"></span>Hexbolt Removal</div>
  </section>

  <section class="card card--front" aria-label="Card front">
    <div class="side-bars"><span></span><span></span></div>

    <div class="wordmark">
      <div class="wordmark__name"><span class="wordmark__square"></span>HEXBOLT REMOVAL</div>
      <div class="wordmark__rule"></div>
      <div class="wordmark__ltd">LTD</div>
    </div>

    <div class="name-plate">
      <div class="name-plate__name">Daniel Whitfield</div>
      <div class="name-plate__title">General Manager</div>
    </div>

    <div class="address-rule"></div>
    <address class="address">
      Foundry Lane, Denton, Manchester<br>M34 9ZZ
      <span class="address__web">www.hexbolt-removal.co.uk</span>
    </address>

    <div class="divider"></div>

    <ul class="contacts">
      <li><svg viewBox="0 0 24 24"><path d="M6.6 10.8a15 15 0 0 0 6.6 6.6l2.2-2.2a1 1 0 0 1 1-.25 11.4 11.4 0 0 0 3.6.57 1 1 0 0 1 1 1V20a1 1 0 0 1-1 1A17 17 0 0 1 3 4a1 1 0 0 1 1-1h3.5a1 1 0 0 1 1 1c0 1.25.2 2.45.57 3.6a1 1 0 0 1-.25 1z"/></svg>0161 555 0182</li>
      <li><svg viewBox="0 0 24 24"><path d="M7 1h10a2 2 0 0 1 2 2v18a2 2 0 0 1-2 2H7a2 2 0 0 1-2-2V3a2 2 0 0 1 2-2zm0 3v14h10V4z"/></svg>07700 900 418</li>
      <li><svg viewBox="0 0 24 24"><path d="M2 5h20v14H2zm2 2v.4l8 5 8-5V7zm0 2.8V17h16V9.8l-8 5z"/></svg>dwhitfield@hexbolt-removal.co.uk</li>
    </ul>

    <div class="foot-accent"></div>
    <div class="foot-band"></div>
  </section>

</body>
</html>
```